Craft Instant Coffee Box Packaging design

We need packaging designed for our craft instant coffee. Needs to be simple yet eye-catching. We are looking to package instant coffee sachets inside a cigarette style box. Front of box must make it clear that it is instant coffee and show contents - 7 pack / 21g net as well as Drift Willow Roasters Co. which is the company name. We'd prefer the instant coffee be the focal point rather than the company name. The rear will have 'ingredients', company address and barcode. Sides should either state contents such as 'Instant Coffee' or company name.

Font styles to use
Sans Serif

Colors

Designer to choose colors to be used in the design.

Requirements
Must have
• Front of box must make it clear that it is instant coffee and show contents - 7 pack / 21g net as well as Drift Willow Roasters Co. which is the company name. We'd prefer the instant coffee be the focal point rather than the company name. The rear will have 'ingredients', company address and barcode. Sides should either state contents such as 'Instant Coffee' or company name.
Nice to have
• modern colour scheme - 'Drift Willow Roasters Co.' in a simple sans serif font
Should not have
• Must not be too 'busy' or 'cheap' looking

```html
<!DOCTYPE html>
<html lang="en">
<head>
<meta charset="utf-8">
<title>Drift Willow Roasters Co. – Instant Coffee Box Front</title>
<link rel="stylesheet" href="https://fonts.googleapis.com/css2?family=Montserrat:wght@500;600;700&display=swap">
<style>
  :root {
    --page: #d4dadb;
    --box-black: #0c0c0c;
    --facet-dark: #151515;
    --facet-mid: #1f1f1f;
    --facet-light: #262626;
    --gold: #8a6437;
    --gold-bright: #d9a93d;
    --cream: #f4f2ee;
    --ink: #111111;
    --white: #ffffff;
  }
  * { box-sizing: border-box; margin: 0; padding: 0; }
  html, body { width: 1200px; height: 789px; overflow: hidden; }
  body {
    background: var(--page);
    font-family: "Montserrat", sans-serif;
    position: relative;
  }
  .box-front {
    position: absolute;
    left: 400px;
    top: 45px;
    width: 400px;
    height: 700px;
    background: var(--box-black);
    overflow: hidden;
  }
  .facets { position: absolute; inset: 0; width: 100%; height: 100%; }
  .brand-mark {
    position: absolute;
    top: 150px;
    left: 0;
    width: 100%;
    display: flex;
    flex-direction: column;
    align-items: center;
    gap: 12px;
  }
  .brand-dot {
    width: 96px;
    height: 96px;
    border-radius: 50%;
    background: var(--gold);
  }
  .brand-name {
    color: var(--gold);
    font-weight: 600;
    font-size: 15px;
    letter-spacing: 1.5px;
    text-transform: uppercase;
  }
  .product-title {
    position: absolute;
    top: 318px;
    left: 0;
    width: 100%;
    text-align: center;
    color: var(--gold);
    font-weight: 600;
    letter-spacing: 7px;
  }
  .product-title span { display: block; font-size: 33px; line-height: 1.1; }
  .product-title .rule {
    width: 220px;
    height: 3px;
    background: var(--gold);
    margin: 6px auto 4px;
  }
  .cup-scene {
    position: absolute;
    left: 0;
    bottom: 0;
    width: 300px;
    height: 300px;
    background:
      radial-gradient(circle at 45% 40%, #a57744 0%, #c9a47a 22%, #eeeae4 40%, #ffffff 62%, var(--cream) 100%);
    clip-path: polygon(0 0, 62% 0, 100% 28%, 100% 100%, 0 100%);
  }
  .net-weight {
    position: absolute;
    left: 34px;
    bottom: 130px;
    color: var(--ink);
    font-weight: 700;
    font-size: 13px;
  }
  .pack-tag {
    position: absolute;
    left: 258px;
    bottom: 10px;
    width: 54px;
    height: 72px;
    background: var(--box-black);
    border-radius: 8px 8px 0 0;
    display: flex;
    align-items: center;
    justify-content: center;
    gap: 2px;
  }
  .pack-tag .count {
    color: var(--gold-bright);
    font-weight: 700;
    font-size: 40px;
    line-height: 1;
  }
  .pack-tag .unit {
    color: var(--white);
    font-weight: 600;
    font-size: 9px;
    writing-mode: vertical-rl;
    transform: rotate(180deg);
    letter-spacing: 1px;
  }
</style>
</head>
<body>
  <main class="box-front">
    <svg class="facets" viewBox="0 0 400 700" aria-hidden="true">
      <polygon points="0,0 400,0 400,120 200,300 0,120" fill="var(--facet-mid)"/>
      <polygon points="60,0 340,0 200,150" fill="var(--facet-light)"/>
      <polygon points="0,120 200,300 0,460" fill="var(--facet-dark)"/>
      <polygon points="400,120 200,300 400,560" fill="var(--facet-dark)"/>
      <polygon points="200,300 400,560 400,700 260,700" fill="var(--box-black)"/>
    </svg>

    <div class="brand-mark">
      <div class="brand-dot"></div>
      <p class="brand-name">Drift Willow Roasters Co.</p>
    </div>

    <h1 class="product-title">
      <span>INSTANT</span>
      <div class="rule"></div>
      <span>COFFEE</span>
    </h1>

    <div class="cup-scene" role="img" aria-label="White cup of latte with heart foam art on a saucer"></div>

    <p class="net-weight">21g</p>

    <div class="pack-tag">
      <span class="count">7</span>
      <span class="unit">PACK</span>
    </div>
  </main>
</body>
</html>
```